Upsell Vertical Banner Ad Design For B2B Marketing Agency Vertical 768px × 1180px IS THE SIZE

I need a banner made for my website www.brightlanepromotionhub.biz This banner will be an upsell advertisement for after someone signs up for my monthly program. When they login to their account for the 1st time I will give them the chance to upgrade their account to our annual program with just one click.

this is a page that upsells it currently to give you an idea how we market ourselves:
https://tlpx.pagevault-example.com/page/tlp-annual-upsell

Use this content:

Are You Ready To Commit To Taking Your Business To The Next Level?

Because We're In This For The Long-Haul and Dedicated To Your Success...

Save $300 By Upgrading To An Annual Membership And Pay Only $74/mth

((BUTTON))Yes, Upgrade My Plan Right Now!

*Must prepay the full year at only $898/yr!

Target Market(s)

business owners

Industry/Entity Type

Marketing

Requirements
Must have
• 768px × 1180px IS THE SIZE vertical

Use this content:

Nice to have
• Use this content:

Should not have
• Use this content:

```html
<!DOCTYPE html>
<html lang="en">
<head>
<meta charset="utf-8">
<title>Annual Membership Upgrade Banner</title>
<link href="https://fonts.googleapis.com/css2?family=Montserrat:wght@600;700;800&display=swap" rel="stylesheet">
<style>
  :root {
    --page-bg: #d6d6d6;
    --brand-blue: #1473c3;
    --brand-blue-dark: #0d66b2;
    --brand-blue-light: #1a7bcc;
    --brand-green: #52d957;
    --text-green: #4fd452;
    --white: #ffffff;
    --button-top: #3b90dc;
    --button-bottom: #0f63ad;
    --photo-a: #c9d3dc;
    --photo-b: #eef2f5;
  }
  * { margin: 0; padding: 0; box-sizing: border-box; }
  html, body {
    width: 900px; height: 1200px; overflow: hidden;
    background: var(--page-bg);
    font-family: "Montserrat", Arial, sans-serif;
  }
  .banner {
    position: absolute; left: 122px; top: 108px;
    width: 655px; height: 982px; overflow: hidden;
    background: var(--white);
  }
  .banner-shapes { position: absolute; inset: 0; }
  .line {
    position: absolute; left: 0; width: 100%;
    text-align: center; font-weight: 800; text-transform: uppercase;
    white-space: nowrap; line-height: 1;
  }
  .headline-ribbon { top: 39px; font-size: 33.5px; color: var(--text-green); }
  .headline-sub { top: 86px; font-size: 26px; color: var(--white); }
  .headline-main { top: 110px; font-size: 74px; color: var(--white); }
  .promise { top: 623px; font-size: 26px; line-height: 30px; color: var(--white); }
  .offer-save { top: 753px; font-size: 36px; color: var(--text-green); }
  .offer-upgrade { top: 786px; font-size: 36.5px; color: var(--brand-blue); }
  .offer-detail { top: 822px; font-size: 17px; color: var(--brand-blue); }
  .offer-detail .price { color: var(--text-green); }
  .divider {
    position: absolute; left: 291px; top: 851px;
    width: 74px; height: 3px; background: var(--text-green);
  }
  .cta-button {
    position: absolute; left: 60px; top: 867px;
    width: 535px; height: 60px; border-radius: 30px;
    background: linear-gradient(to bottom, var(--button-top), var(--button-bottom));
    color: var(--white); font-size: 27.5px; font-weight: 700;
    display: flex; align-items: center; justify-content: center;
    text-decoration: none; white-space: nowrap;
  }
  .fine-print {
    top: 936px; font-size: 20.5px; font-weight: 600;
    color: var(--text-green); text-transform: none;
  }
</style>
</head>
<body>
  <section class="banner">
    <svg class="banner-shapes" width="655" height="982" viewBox="0 0 655 982">
      <defs>
        <linearGradient id="photoTone" x1="0" y1="0" x2="1" y2="1">
          <stop offset="0" stop-color="var(--photo-b)"/>
          <stop offset="1" stop-color="var(--photo-a)"/>
        </linearGradient>
      </defs>
      <rect class="sky-band" width="655" height="982" fill="var(--brand-blue-dark)"/>
      <circle class="sky-glow" cx="330" cy="470" r="340" fill="var(--brand-blue-light)"/>
      <path class="green-wave" fill="var(--brand-green)"
        d="M0,455 C120,430 260,470 380,470 C480,470 580,440 655,445 L655,982 L0,982 Z"/>
      <path class="white-base" fill="var(--white)"
        d="M0,792 C90,788 160,752 260,742 C380,732 520,728 590,708 C620,700 640,680 655,668 L655,982 L0,982 Z"/>
      <path class="ribbon" fill="var(--white)"
        d="M28,32 L628,32 L608,55 L628,78 L28,78 L48,55 Z"/>
      <path class="photo-frame" role="img"
        aria-label="Photo: a business team in a bright office giving each other high-fives around a table with laptops"
        fill="url(#photoTone)" stroke="var(--white)" stroke-width="6"
        d="M80,360 C85,250 200,232 300,226 C400,220 450,186 520,196 C585,206 588,300 577,372 C565,455 530,560 420,596 C330,622 170,602 110,540 C80,505 76,420 80,360 Z"/>
      <path class="photo-swoosh" fill="var(--white)"
        d="M82,300 C120,250 200,235 300,228 C230,250 160,270 85,345 Z"/>
    </svg>

    <p class="line headline-ribbon">Are you ready to commit</p>
    <p class="line headline-sub">To taking your business to the</p>
    <h1 class="line headline-main">Next Level?</h1>

    <p class="line promise">Because we're<br>in this for the long-haul<br>and dedicated to your success...</p>

    <p class="line offer-save">Save $300</p>
    <p class="line offer-upgrade">By upgrading to an</p>
    <p class="line offer-detail">Annual membership and pay only <span class="price">$74/mth</span></p>
    <div class="divider"></div>

    <a class="cta-button" href="#">Yes, Upgrade My Plan Right Now!</a>

    <p class="line fine-print">*Must prepay the full year at only $898/yr!</p>
  </section>
</body>
</html>
```